Design a thanksgiving seasonal promotional banner ad for a spa

We need a promotional banner ad to be placed on social media and around the web.

There is no specific size requirement you can also make it in the square as long as your work quality is good.

The banner should have a lifestyle picture relating to the subject and also nice and clear typography.

We need the following info to be on the banner.
* Logo (get it from the website or yelp)
* A nice lifestyle photography relating to the promotion.
* website address (velvetgrovespa.com)
* Social media icons
* Phone Number (Get it from the website)
* Address(get it from the website)
* Promo text

Limited time only
Our Thanksgiving Promotions
Couple massage: $88/h (Original price:$100/h)
$10 off for Anti-Aging Facial (Original price:$60/h)
Semi-permanent makeup on eyebrows, special price: $200 (Original price:$280-$680)

Feel free to modify and fix the text to make sense to you and your design. This is just the raw facts about the promotion. so feel free to make it fancy.

Final work should be open layered royalty free
PSD or Ai format is accepted.

The winner will be hired for other ongoing projects as well.

```html
<!DOCTYPE html>
<html lang="en">
<head>
<meta charset="utf-8">
<title>Velvet Grove Spa – Thanksgiving Promotions</title>
<link rel="stylesheet" href="https://fonts.googleapis.com/css2?family=Oswald:wght@500;600&family=Roboto+Condensed:wght@400;500;700&display=swap">
<style>
  :root {
    --brown: #4a2a17;
    --green: #7ac143;
    --white: #ffffff;
    --ink: #3a2a20;
    --page: #e4e4e4;
    --skin-light: #e9c7b8;
    --skin-mid: #c99a84;
    --skin-dark: #8a6656;
  }
  * { margin: 0; padding: 0; box-sizing: border-box; }
  html, body { width: 1200px; height: 1200px; overflow: hidden; background: var(--page); }
  .banner {
    position: absolute; left: 40px; top: 204px;
    width: 1120px; height: 791px;
    background: var(--white); overflow: hidden;
    font-family: "Roboto Condensed", "Arial Narrow", sans-serif; color: var(--ink);
  }
  .shapes { position: absolute; inset: 0; }
  .brand {
    position: absolute; left: 48px; top: 62px;
    display: flex; align-items: center; gap: 12px;
    font-weight: 500; font-size: 32px; color: var(--brown);
  }
  .brand-dot { width: 30px; height: 30px; border-radius: 50%; background: var(--green); }
  .headline {
    position: absolute; left: 48px; top: 148px;
    font-family: "Oswald", "Arial Narrow", sans-serif; font-weight: 600;
    font-size: 60px; line-height: 68px; color: var(--brown); text-transform: uppercase;
  }
  .headline .accent { color: var(--green); }
  .offer { position: absolute; }
  .offer-title { font-weight: 700; font-size: 17px; text-transform: uppercase; letter-spacing: .2px; }
  .offer-rule { width: 58px; height: 3px; background: var(--green); margin: 9px 0 24px; }
  .offer-price {
    font-family: "Oswald", "Arial Narrow", sans-serif; font-weight: 600;
    font-size: 36px; line-height: 38px; color: var(--green);
  }
  .offer-note { font-size: 16px; line-height: 20px; }
  .offer--massage { left: 48px; top: 314px; }
  .offer--facial { left: 250px; top: 314px; }
  .feature-band {
    position: absolute; left: 0; top: 469px; width: 618px; height: 184px;
    background: var(--brown); color: var(--white);
  }
  .offer--brows { left: 48px; top: 30px; }
  .offer--brows .offer-rule { margin-bottom: 14px; }
  .offer-label { font-weight: 700; font-size: 16px; color: var(--green); text-transform: uppercase; }
  .contact {
    position: absolute; left: 48px; top: 698px;
    font-size: 17px; line-height: 27px; color: var(--ink);
  }
  .badge-text {
    font-family: "Oswald", "Arial Narrow", sans-serif; font-weight: 500;
    font-size: 26px; fill: var(--white);
  }
</style>
</head>
<body>
  <main class="banner">
    <svg class="shapes" width="1120" height="791" viewBox="0 0 1120 791">
      <defs>
        <linearGradient id="treatment-tones" x1="0" y1="0" x2="1" y2="1">
          <stop offset="0" stop-color="var(--skin-dark)"/>
          <stop offset=".35" stop-color="var(--skin-light)"/>
          <stop offset=".7" stop-color="var(--skin-mid)"/>
          <stop offset="1" stop-color="var(--skin-dark)"/>
        </linearGradient>
      </defs>
      <polygon role="img" aria-label="Photo of a beautician applying semi-permanent eyebrow makeup to a relaxed client"
               points="618,0 1120,0 1120,791 838,791 618,316" fill="url(#treatment-tones)"/>
      <polygon points="399,0 500,0 618,316" fill="var(--brown)"/>
      <polygon points="500,0 618,0 618,316" fill="var(--green)"/>
      <polygon points="618,316 618,791 743,791" fill="var(--green)"/>
      <polygon points="618,316 743,791 838,791" fill="var(--brown)"/>
    </svg>

    <div class="brand"><span class="brand-dot"></span>Velvet Grove Spa</div>

    <h1 class="headline"><span>Our </span><span class="accent">Thanksgiving</span><br>Promotions</h1>

    <section class="offer offer--massage">
      <h2 class="offer-title">Couple Massage</h2>
      <div class="offer-rule"></div>
      <p class="offer-price">$88/h</p>
      <p class="offer-note">(Original Price: $100/h)</p>
    </section>

    <section class="offer offer--facial">
      <h2 class="offer-title">Anti-Aging Facial</h2>
      <div class="offer-rule"></div>
      <p class="offer-price">$10 OFF</p>
      <p class="offer-note">(Original Price: $60/h)</p>
    </section>

    <section class="feature-band">
      <div class="offer offer--brows">
        <h2 class="offer-title">Semi-Permanent Makeup on Eyebrows</h2>
        <div class="offer-rule"></div>
        <p class="offer-label">Special Price:</p>
        <p class="offer-price">$200</p>
        <p class="offer-note">(Original Price: $280-$680)</p>
      </div>
    </section>

    <address class="contact" style="font-style:normal">
      555-214-7730 | info@velvetgrovespa.com | velvetgrovespa.com<br>
      410 N. Maple Crest Ave., Fairview, CA 90210
    </address>

    <svg class="shapes" width="1120" height="791" viewBox="0 0 1120 791" aria-label="Limited time only">
      <circle cx="611" cy="376" r="82" fill="var(--green)"/>
      <circle cx="611" cy="376" r="66" fill="none" stroke="var(--white)" stroke-width="4"/>
      <text class="badge-text" x="611" y="370" text-anchor="middle">LIMITED</text>
      <text class="badge-text" x="611" y="402" text-anchor="middle">TIME ONLY</text>
    </svg>
  </main>
</body>
</html>
```